Can you make FairlyNeat look better than average? We need business cards and a logo refresh :-)

REVISED BRIEF

PRIORITY

VECTOR LOGO

Create a vector version of our existing logo. The logo must not change from its current design, weight or font.

Deliverables

- Logo in blue (#2540BB)
- Logo in white (#FFFFFF)
- Logo in grey (#36454F)
- All logos on transparent background
- All logos in PNG & SVG formats. (SVG must NOT distort stroke width when resized)

BRAND MARK

Create a brand mark for use with the logo. This should be possible to used with the logo and on its own as a stand alone graphical device that represents the FAIRLYNEAT brand.

https://quellbrik.com/resources/glossary/what-is-a-brand-mark

Deliverables

- Brand Mark in blue (#2540BB)
- Brand Mark in white (#FFFFFF)
- Brand Mark in grey (#36454F)
- Brand Mark on transparent background
- Brand Mark in PNG & SVG formats. (SVG must NOT distort stroke width when resized)
- Logo combined with Brand Mark (colours and formats)
.

Business Card Layout

Create 2 layouts with the following details:-

Marcus Delaney
Co-Founder & Chief Product Officer

marcus@fairlyneat.nz
www.fairlyneat.nz
0279831465

Callum Ferris
Founder & CEO

hello@fairlyneat.nz
www.fairlyneat.nz
021 684 2590

DESIGN CONSIDERATIONS

Create versions with ‘Shaping Causes With Heart’ tag line incorporated within the design and without (maintain separation of logo from tag line)

- Create a version with and without the brand mark
- Keep it clean and simple but elevate the design with subtle design effects
- Consider use of raised spot gloss colour (this can be white on white for subtle or blue on blue or blue on white)
- Consider use of spot gloss colour (this can be white on white for subtle or blue on blue or blue on white)
- Consider use of letterpress indentation
- Ensure contact details are legible, use sans-serif font

PREVIOUS BRIEF

We need a business card design for our business FairlyNeat. We are a purpose driven brand and media agency that helps brands and charities plan and buy traditional media campaigns (TV, Radio, Print, Outdoor etc). We give a significant amount of the media booking fees we receive from media vendors to charity in the name of our clients. https://www.plinkwork.com/posts/wearefairlyneat_giveback-fairlyneat-shapingcauseswithheart-activity-5829170364418205731-Rtqe

Our strapline is 'Shaping Causes With Heart'.

We want to keep our logo design as it is but it does need tightening up and made into a proper vector image as it's been created from a font.

Our brand colour is #2540BB and we need to keep this.

Our brand is professional but human, warm and engaging and doesn't take itself too seriously.

Things We Need
- vectorisation and tidying up of existing logo
- We'd like you to think about how we can incorporate a brand mark with the logo to add another dimension to our brand
- business card layout and design
- we'll be using zentiprint.com to print the cards so please take a look at the options they have (spot gloss, foil, letterpress, square cards and even the backs of the cards can have a different design on every single card!
- potential opportunity for different famous quotes on the back or imagery or slight design differences
- we'd be open to the use of an emoji or emojiis as the brandmark or to be incorporated into the card designs
- we can have as many different design batches as we like for the backs of the cards

https://www.zentiprint.com/au/business-cards

We want to make an impact, we want to be seen as professional but fun, we want to be different.

Here's a press release of what we're about.

https://adwirely.co.nz/movings-shakings/fairlyneat-welcomes-marcus-delaney-as-co-founder/

Be bold, be different, there is no such thing as a bad idea. We're open to anything so please bring your best ideas and have fun with it! Go crazy if you like!
____________
Marcus Delaney
marcus@fairlyneat.nz
0279831465

Callum Ferris
Founder & CEO
hello@fairlyneat.nz
021 684 2590

Shaping Causes With Heart

________

These are the only details we MUST have on the cards, the rest is up to you. Just make sure you use all of your creativity but don't feel the need to crowd the card with too much, let it breathe as well.

In terms of font for the details, we'll leave that up to you, just ensure it's legible. Oh and please don't take any design inspiration from our website - that will be changing!

Please don't let the design and layout look cheap and tacky though. It needs to still feel premium but personable.

Thanks

Marcus

Many designs are changing the logo and this was NOT in the brief. We need a brand mark to complement the logo. We need to see the logo with and without the brand mark. We need to see the business card with both logo + brand mark and logo on its own We need to see the business card with and without the tagline 'Shaping Causes With Heart'

purpose driven Brand & Media Agency

Shaping Causes With Heart
Marcus Delaney, Co-Founder & Chief Product Officer, marcus@fairlyneat.nz fairlyneet.nz, 0279 831 465

Callum Ferris, Founder & CEO hello@fairlyneat.nz, fairlyneet.nz, 021 684 2590

Serif
Sans Serif

0054AA
0677BA
7BADD7
CADEEF
E8F1F8

• brand mark, vector version of existing logo, Shaping Causes With Heart tagline, existing logo traced and vectorised. Must fully explore the design options from zentiprint.com that can enhance the overall card design
• brandmark to help elevate the logo, maybe incorporate some other design elements into the card like lines, or grids.
• A cheap look and feel

```html
<!DOCTYPE html>
<html lang="en">
<head>
<meta charset="utf-8">
<title>FairlyNeat – Business Card</title>
<link rel="stylesheet" href="https://fonts.googleapis.com/css2?family=Open+Sans:wght@400;600;700&display=swap">
<style>
  :root {
    --page-bg: #e4dccf;
    --frost: #d8d1c5;
    --frost-edge: #c9bfae;
    --panel-blue: #1f1e74;
    --panel-blue-light: #2b2d86;
    --ink-navy: #28287a;
    --sand: #d9ccb4;
  }
  * { margin: 0; padding: 0; box-sizing: border-box; }
  html, body {
    width: 1200px;
    height: 1046px;
    overflow: hidden;
    background: var(--page-bg);
  }
  .card {
    position: absolute;
    left: 60px;
    top: 230px;
    width: 1080px;
    height: 587px;
    border-radius: 40px;
    background: var(--frost);
    border: 2px solid var(--frost-edge);
    overflow: hidden;
  }
  .card__panel {
    position: absolute;
    left: 180px;
    top: 0;
    right: 0;
    bottom: 0;
    background: linear-gradient(135deg, var(--panel-blue-light) 0%, var(--panel-blue) 45%, var(--panel-blue) 100%);
  }
  .brand {
    position: absolute;
    left: -150px;
    top: 236px;
    width: 486px;
    height: 112px;
    transform: rotate(-90deg);
    display: flex;
    flex-direction: column;
    align-items: flex-start;
    justify-content: center;
    font-family: 'Open Sans', sans-serif;
    color: var(--ink-navy);
  }
  .brand__name {
    font-weight: 700;
    font-size: 60px;
    line-height: 1;
    white-space: nowrap;
  }
  .brand__tagline {
    margin-top: 10px;
    font-weight: 600;
    font-size: 16px;
    letter-spacing: 5.4px;
    white-space: nowrap;
  }
  .person {
    position: absolute;
    right: 38px;
    top: 300px;
    text-align: right;
    font-family: 'Open Sans', sans-serif;
    color: var(--sand);
  }
  .person__name {
    font-weight: 700;
    font-size: 46px;
    line-height: 1.1;
  }
  .person__role {
    font-weight: 600;
    font-size: 22px;
    margin-top: 2px;
  }
  .name-bar {
    position: absolute;
    right: 0;
    top: 305px;
    width: 26px;
    height: 82px;
    background: var(--sand);
  }
  .contacts {
    position: absolute;
    right: 38px;
    top: 446px;
    list-style: none;
    font-family: 'Open Sans', sans-serif;
    font-size: 22px;
    color: var(--sand);
  }
  .contacts__item {
    display: flex;
    align-items: center;
    justify-content: flex-end;
    gap: 12px;
    height: 35px;
  }
  .contacts__icon { width: 22px; height: 22px; }
</style>
</head>
<body>
  <div class="card">
    <div class="brand">
      <div class="brand__name">FAIRLYNEAT</div>
      <div class="brand__tagline">SHAPING CAUSES WITH HEART</div>
    </div>

    <div class="card__panel">
      <div class="person">
        <div class="person__name">Callum Ferris</div>
        <div class="person__role">Founder &amp; CEO</div>
      </div>
      <div class="name-bar"></div>

      <ul class="contacts">
        <li class="contacts__item">
          <span>021 684 2590</span>
          <svg class="contacts__icon" viewBox="0 0 24 24" aria-hidden="true">
            <path fill="#d9ccb4" d="M6.6 2.5l3 3.2-1.8 2.4c1.2 2.6 3.4 4.8 6 6l2.4-1.8 3.2 3-1.7 3.2C12 18.3 5.6 11.9 3.5 4.2z"/>
            <path fill="none" stroke="#d9ccb4" stroke-width="1.8" stroke-linecap="round" d="M14 3.5a7 7 0 0 1 6.5 6.5M14 7a3.5 3.5 0 0 1 3 3"/>
          </svg>
        </li>
        <li class="contacts__item">
          <span>www.fairlyneat.nz</span>
          <svg class="contacts__icon" viewBox="0 0 24 24" aria-hidden="true">
            <circle cx="12" cy="12" r="10" fill="#d9ccb4"/>
            <path fill="none" stroke="#1f1e74" stroke-width="1.5" d="M2 12h20M12 2c3 3 3 17 0 20M12 2c-3 3-3 17 0 20"/>
          </svg>
        </li>
        <li class="contacts__item">
          <span>hello@fairlyneat.nz</span>
          <svg class="contacts__icon" viewBox="0 0 24 24" aria-hidden="true">
            <path fill="#d9ccb4" d="M2 10l10-7 10 7v11H2z"/>
            <rect x="6" y="6" width="12" height="9" fill="#1f1e74"/>
            <circle cx="12" cy="10.5" r="2.3" fill="none" stroke="#d9ccb4" stroke-width="1.2"/>
            <path fill="none" stroke="#1f1e74" stroke-width="1.3" d="M2 10l10 7 10-7M2 21l7-6M22 21l-7-6"/>
          </svg>
        </li>
      </ul>
    </div>
  </div>
</body>
</html>
```